Weightloss company needs Business Card

We want a business card that is clean and professional, yet portrays that we are a friendly, innovative, and versatile program designed to fit the needs of our clients.
I would like there to be 2 sides, one side having an appointment card, and the other side containing the logo and business information. There can be decorations on both sides. The logo is attached.

Target Market(s)

Men and women 40-60

Industry/Entity Type

Business

Contact Information for Business Card

Font styles to use
Sans Serif

Requirements
Must have
• The logo, space for business information
Nice to have
• The colors in the logo
Should not have
• No pictures of people or food

```html
<!DOCTYPE html>
<html lang="en">
<head>
<meta charset="utf-8">
<title>Brightturn Weightloss – Business Card</title>
<link href="https://fonts.googleapis.com/css2?family=Open+Sans:wght@400;600;700;800&display=swap" rel="stylesheet">
<style>
  :root {
    --backdrop: #b9babd;
    --paper: #ffffff;
    --teal-light: #5fbfcd;
    --teal-dark: #4a939e;
    --stripe-grey: #8c8d8f;
    --rule-grey: #e4e6e8;
    --text-grey: #76777a;
    --brand-red: #e31b3a;
  }
  * { box-sizing: border-box; margin: 0; padding: 0; }
  html, body {
    width: 1200px; height: 1200px; overflow: hidden;
    background: var(--backdrop);
    font-family: "Open Sans", Arial, sans-serif;
  }
  .sheet {
    width: 1200px; height: 1200px;
    display: flex; flex-direction: column; align-items: center; justify-content: center;
    gap: 40px;
  }
  .card {
    position: relative;
    width: 900px; height: 514px;
    background: var(--paper);
    overflow: hidden;
    box-shadow: 0 10px 26px rgba(0,0,0,0.18);
  }
  .card__art { position: absolute; inset: 0; width: 100%; height: 100%; }

  /* Appointment side */
  .appointment__title {
    position: absolute; top: 52px; right: 58px;
    color: var(--paper); font-weight: 700; font-size: 44px; letter-spacing: 1.5px;
  }

  /* Identity side */
  .identity__name {
    position: absolute; top: 34px; left: 44px; color: var(--paper);
  }
  .identity__name h1 { font-weight: 400; font-size: 44px; line-height: 1.1; }
  .identity__name p { font-weight: 400; font-size: 24px; line-height: 1.2; }

  .brand {
    position: absolute; left: 50px; top: 318px;
    display: flex; align-items: center; gap: 18px;
  }
  .brand__name {
    color: var(--brand-red); font-weight: 800; font-size: 50px; line-height: 1.0;
  }
  .brand__dot {
    width: 30px; height: 30px; border-radius: 50%; background: var(--brand-red);
  }

  .contact {
    position: absolute; right: 44px; top: 300px;
    list-style: none; text-align: right; color: var(--text-grey);
    font-size: 24px; line-height: 1.3;
  }
  .contact li { display: flex; justify-content: flex-end; align-items: center; gap: 10px; }
  .contact li.contact__address { margin-top: 14px; align-items: center; }
  .contact__icon { width: 20px; height: 20px; flex: none; }
</style>
</head>
<body>
<main class="sheet">

  <!-- Appointment side -->
  <section class="card appointment">
    <svg class="card__art" viewBox="0 0 900 514" aria-hidden="true">
      <defs>
        <linearGradient id="tealBack" x1="0" y1="0" x2="1" y2="1">
          <stop offset="0" stop-color="var(--teal-dark)"/>
          <stop offset="1" stop-color="var(--teal-light)"/>
        </linearGradient>
      </defs>
      <g transform="translate(-30,12)">
        <path fill="var(--stripe-grey)" d="M0,0 H930 V514 H720 C600,380 470,120 300,60 C200,28 80,20 0,22 Z"/>
      </g>
      <g transform="translate(-16,6)">
        <path fill="var(--paper)" d="M0,0 H930 V514 H720 C600,380 470,120 300,60 C200,28 80,20 0,22 Z"/>
      </g>
      <path fill="url(#tealBack)" d="M0,0 H900 V514 H720 C600,380 470,120 300,60 C200,28 80,20 0,22 Z"/>
      <g class="appointment__rules" stroke="var(--rule-grey)" stroke-width="2">
        <line x1="40" y1="190" x2="470" y2="190"/>
        <line x1="40" y1="260" x2="540" y2="260"/>
        <line x1="40" y1="330" x2="590" y2="330"/>
        <line x1="40" y1="400" x2="630" y2="400"/>
      </g>
    </svg>
    <h2 class="appointment__title">Appointments</h2>
  </section>

  <!-- Identity side -->
  <section class="card identity">
    <svg class="card__art" viewBox="0 0 900 514" aria-hidden="true">
      <defs>
        <linearGradient id="tealFront" x1="0" y1="0" x2="1" y2="0">
          <stop offset="0" stop-color="var(--teal-light)"/>
          <stop offset="1" stop-color="var(--teal-dark)"/>
        </linearGradient>
      </defs>
      <path fill="var(--stripe-grey)" d="M0,0 H900 V266 C640,240 330,250 0,290 Z"/>
      <path fill="var(--paper)" d="M0,0 H900 V248 C640,226 340,236 0,284 Z"/>
      <path fill="url(#tealFront)" d="M0,0 H900 V232 C650,214 350,226 0,280 Z"/>
    </svg>

    <div class="identity__name">
      <h1>John Doe</h1>
      <p>Director</p>
    </div>

    <div class="brand">
      <div class="brand__name">Brightturn<br>Weightloss</div>
      <span class="brand__dot"></span>
    </div>

    <ul class="contact">
      <li>111.222.3333
        <svg class="contact__icon" viewBox="0 0 20 20" aria-label="Phone"><circle cx="10" cy="10" r="10" fill="var(--brand-red)"/><path d="M6 5.5c1-.6 1.6.3 2 1.2.3.6 0 1-.5 1.4.5 1.3 1.3 2.1 2.5 2.7.4-.5.8-.8 1.4-.5.9.4 1.8 1 1.2 2-.9 1.5-3.2.9-5-.9S4.5 6.4 6 5.5z" fill="#fff"/></svg></li>
      <li>111.222.3333
        <svg class="contact__icon" viewBox="0 0 20 20" aria-label="Fax"><circle cx="10" cy="10" r="10" fill="var(--brand-red)"/><rect x="7" y="5" width="6" height="3" fill="#fff"/><rect x="5" y="8.5" width="10" height="5" rx="1" fill="#fff"/><rect x="7" y="12" width="6" height="3" fill="#fff" stroke="var(--brand-red)" stroke-width=".8"/></svg></li>
      <li>www.brightturn.com
        <svg class="contact__icon" viewBox="0 0 20 20" aria-label="Website"><circle cx="10" cy="10" r="10" fill="var(--brand-red)"/><circle cx="10" cy="10" r="5" fill="none" stroke="#fff" stroke-width="1.4"/><path d="M5 10h10M10 5c-2 2.8-2 7.2 0 10M10 5c2 2.8 2 7.2 0 10" fill="none" stroke="#fff" stroke-width="1.1"/></svg></li>
      <li>info@brightturn.com
        <svg class="contact__icon" viewBox="0 0 20 20" aria-label="Email"><circle cx="10" cy="10" r="10" fill="var(--brand-red)"/><rect x="5" y="6.5" width="10" height="7" rx="1" fill="#fff"/><path d="M5.5 7l4.5 3.5L14.5 7" fill="none" stroke="var(--brand-red)" stroke-width="1"/></svg></li>
      <li class="contact__address"><span>Dummy City<br>Dummy Country Land</span>
        <svg class="contact__icon" viewBox="0 0 20 20" aria-label="Address"><circle cx="10" cy="10" r="10" fill="var(--brand-red)"/><path d="M10 15.5s-4-4.2-4-7a4 4 0 0 1 8 0c0 2.8-4 7-4 7z" fill="#fff"/><circle cx="10" cy="8.5" r="1.5" fill="var(--brand-red)"/></svg></li>
    </ul>
  </section>

</main>
</body>
</html>
```